electrical contractor business card for professional modern company

I need a business card design for an electrical contractors business. I do all kinds of electricical work from new homes, air conditioning, data and communications. I have a logo design i want on it and have a good idea in my head of what i want it to look like. I like simple yet bold and professional looking. All black background is a must

Target Market(s)

Anyone needing electrical work done

Industry/Entity Type

Electrical

Contact Information for Business Card

company name- KTW Electrical and Data
person name-martin pellowe
phone number- 0418 362 927
website-ktwelec.example.com.au

Font styles to use
Sans Serif

Requirements
Must have
• email
• website
• logo
• name
• phone number
• list of work i do:
• -electrical
• -air-conditioning
• -data/communications
• -cctv/security
• -domestic/commercial/industrial
• -24hr emergency breakdown repair
Nice to have
• i would like the logo on the front side in the centre taking up most of the card with black background.
• on the rear i want the list of work i do with company info i.e. email, website, my name, phone number. rear of card also black background with orange writing to match the orange in the logo

```html
<!DOCTYPE html>
<html lang="en">
<head>
<meta charset="utf-8">
<title>KTW Electrical and Data – Business Card</title>
<link rel="stylesheet" href="https://fonts.googleapis.com/css2?family=Varela+Round&display=swap">
<style>
  :root {
    --backdrop: #d9d3c9;
    --card-black: #0b0b0b;
    --card-edge: #1c1c1c;
    --orange: #f06a22;
    --ink-dark: #111111;
    --divider: #e2611d;
  }
  * { box-sizing: border-box; margin: 0; padding: 0; }
  html, body {
    width: 1200px;
    height: 1000px;
    overflow: hidden;
    background: var(--backdrop);
    font-family: "Varela Round", Arial, sans-serif;
  }
  .canvas {
    position: relative;
    width: 1200px;
    height: 1000px;
  }
  .card {
    position: absolute;
    width: 640px;
    height: 366px;
    background: var(--card-black);
    border: 1px solid var(--card-edge);
    box-shadow: 0 14px 30px rgba(0,0,0,0.35);
    overflow: hidden;
  }

  /* Rear card */
  .card--rear { left: 60px; top: 70px; }
  .name-bar {
    position: absolute;
    left: 0; top: 30px;
    width: 250px; height: 40px;
    background: var(--orange);
    color: var(--ink-dark);
    font-size: 22px;
    line-height: 40px;
    padding-left: 28px;
  }
  .contact-list {
    position: absolute;
    left: 30px; top: 88px;
    list-style: none;
  }
  .contact-item {
    display: flex;
    align-items: center;
    gap: 14px;
    height: 28px;
    color: var(--orange);
    font-size: 16px;
  }
  .contact-icon { width: 20px; height: 20px; flex: none; }
  .section-divider {
    position: absolute;
    left: 0; top: 182px;
    width: 400px; height: 2px;
    background: var(--divider);
  }
  .services-bar {
    position: absolute;
    left: 0; top: 206px;
    width: 180px; height: 34px;
    background: var(--orange);
    color: var(--ink-dark);
    font-size: 20px;
    line-height: 34px;
    padding-left: 28px;
  }
  .services-list {
    position: absolute;
    left: 30px; top: 250px;
    list-style: none;
    columns: 2;
    column-gap: 24px;
    width: 560px;
  }
  .service {
    display: flex;
    align-items: center;
    gap: 10px;
    color: var(--orange);
    font-size: 18px;
    height: 26px;
    break-inside: avoid;
  }
  .service::before {
    content: "";
    width: 10px; height: 10px;
    border: 1.5px solid var(--orange);
    border-radius: 50%;
    flex: none;
  }
  .rear-brand {
    position: absolute;
    right: 30px; top: 118px;
    width: 190px;
    text-align: center;
    color: var(--orange);
    font-size: 17px;
    line-height: 1.3;
  }

  /* Front card */
  .card--front {
    left: 500px; top: 560px;
    display: flex;
    align-items: center;
    justify-content: center;
    gap: 18px;
  }
  .front-dot {
    width: 34px; height: 34px;
    border-radius: 50%;
    background: var(--orange);
    flex: none;
  }
  .front-brand {
    color: var(--orange);
    font-size: 36px;
    letter-spacing: 1px;
  }
</style>
</head>
<body>
<main class="canvas">

  <section class="card card--rear" aria-label="Rear of business card">
    <div class="name-bar">Martin Pellowe</div>

    <ul class="contact-list">
      <li class="contact-item">
        <svg class="contact-icon" viewBox="0 0 20 20" aria-hidden="true">
          <circle cx="10" cy="10" r="9.5" fill="#f06a22"/>
          <path d="M6.5 5.5c.6-.6 1.4-.5 1.8.1l.9 1.4c.3.5.2 1-.2 1.4l-.6.5c.5 1.2 1.4 2.1 2.6 2.6l.5-.6c.4-.4.9-.5 1.4-.2l1.4.9c.6.4.7 1.2.1 1.8-1 1-2.6 1.2-4.6-.3-1.5-1.1-2.6-2.3-3.3-3.8-.8-1.7-.8-3 0-3.8z" fill="#0b0b0b"/>
        </svg>
        0418 362 927
      </li>
      <li class="contact-item">
        <svg class="contact-icon" viewBox="0 0 20 20" aria-hidden="true">
          <circle cx="10" cy="10" r="9.5" fill="#f06a22"/>
          <rect x="5" y="6.5" width="10" height="7" fill="#0b0b0b"/>
          <path d="M5 6.5l5 4 5-4" stroke="#f06a22" stroke-width="1" fill="none"/>
        </svg>
        pellowe@ktwelec.example.com.au
      </li>
      <li class="contact-item">
        <svg class="contact-icon" viewBox="0 0 20 20" aria-hidden="true">
          <circle cx="10" cy="10" r="9.5" fill="#f06a22"/>
          <circle cx="10" cy="10" r="5.5" fill="none" stroke="#0b0b0b" stroke-width="1.2"/>
          <ellipse cx="10" cy="10" rx="2.4" ry="5.5" fill="none" stroke="#0b0b0b" stroke-width="1"/>
          <path d="M4.5 10h11M5.3 7.2h9.4M5.3 12.8h9.4" stroke="#0b0b0b" stroke-width="1"/>
        </svg>
        www.ktwelec.example.com.au
      </li>
    </ul>

    <div class="section-divider"></div>

    <div class="rear-brand">KTW Electrical and Data</div>

    <div class="services-bar">Services</div>
    <ul class="services-list">
      <li class="service">electrical</li>
      <li class="service">air-conditioning</li>
      <li class="service">data/ communications</li>
      <li class="service">cctv/ security</li>
      <li class="service">domestic/commercial/</li>
      <li class="service">industrial</li>
      <li class="service">24hr emergency</li>
      <li class="service">breakdown repair</li>
    </ul>
  </section>

  <section class="card card--front" aria-label="Front of business card">
    <span class="front-dot" aria-hidden="true"></span>
    <span class="front-brand">KTW Electrical and Data</span>
  </section>

</main>
</body>
</html>
```